A label for my commercially sold local honey. This is a LABEL not a logo

3 inches high
2 inches wide

Target Market(s)

Customers who like "local" honey

Logo Text

Wildflower Honey -- 100% Pure & Unfiltered -- Florida

Logo styles of interest
Wordmark Logo
Requirements
Must have
• Wildflower Honey -- 100% Pure & Unfiltered -- Florida

Florida should be dominant

3 inches high / 2 inches wide

```html
<!DOCTYPE html>
<html lang="en">
<head>
<meta charset="utf-8">
<title>Wildflower Honey Label</title>
<link rel="stylesheet" href="https://fonts.googleapis.com/css2?family=Cormorant+Garamond:wght@400;500;600;700&family=Pinyon+Script&display=swap">
<style>
  :root {
    --cream: #fffce6;
    --ink: #111111;
    --paper: #ffffff;
    --floral-light: #ecebdc;
    --floral-dark: #8e8d84;
  }
  * { box-sizing: border-box; margin: 0; padding: 0; }
  html, body { width: 1200px; height: 626px; overflow: hidden; background: var(--cream); }
  body { font-family: "Cormorant Garamond", Georgia, serif; color: var(--ink); }
  .label { position: relative; width: 1200px; height: 626px; background: var(--cream); }

  /* Left wrap panel */
  .story { position: absolute; left: 39px; top: 84px; width: 233px; height: 396px;
           border-top: 2px solid var(--ink); border-bottom: 2px solid var(--ink); text-align: center; }
  .story-title { font-family: "Pinyon Script", cursive; font-weight: 400; font-size: 24px; margin-top: 24px; }
  .story p { font-size: 16.5px; line-height: 21.5px; margin: 14px 18px 0; }
  .story p + p { margin-top: 20px; }

  /* Front panel: 2 in wide by 3 in high (408 x 612) */
  .floral-field { position: absolute; left: 285px; top: 0; width: 618px; height: 626px;
                  background: radial-gradient(ellipse at 40% 60%, var(--floral-dark) 0%, var(--floral-light) 60%, var(--cream) 100%); }
  .front-panel { position: absolute; left: 403px; top: 7px; width: 408px; height: 612px; border: 1px solid var(--ink); }
  .front-card { position: absolute; left: 426px; top: 127px; width: 362px; height: 364px; background: var(--paper); text-align: center; }
  .corner { position: absolute; width: 38px; height: 30px; border-color: var(--ink); border-style: solid; border-width: 0; }
  .corner.tl { left: 14px; top: 14px; border-top-width: 2px; border-left-width: 2px; }
  .corner.tr { right: 14px; top: 14px; border-top-width: 2px; border-right-width: 2px; }
  .corner.bl { left: 14px; bottom: 14px; border-bottom-width: 2px; border-left-width: 2px; }
  .corner.br { right: 14px; bottom: 14px; border-bottom-width: 2px; border-right-width: 2px; }
  .brand-name { position: absolute; left: 0; right: 0; top: 30px; font-size: 20px; font-weight: 700; letter-spacing: 1px; line-height: 24px; }
  .brand-mark { display: block; width: 12px; height: 12px; margin: 0 auto 6px; background: var(--ink); border-radius: 50%; }
  .divider { position: absolute; left: 39px; right: 40px; top: 90px; border-top: 2px solid var(--ink); }
  .product { position: absolute; left: 0; right: 0; top: 100px; font-size: 48px; font-weight: 500; letter-spacing: 12px; padding-left: 12px; line-height: 1; }
  .variety { position: absolute; left: 0; right: 0; top: 154px; font-family: "Pinyon Script", cursive; font-size: 28px; line-height: 1.1; }
  .claim { position: absolute; left: 0; right: 0; top: 194px; font-size: 19px; font-weight: 700; line-height: 1.2; }
  .origin { position: absolute; left: 0; right: 0; top: 226px; font-size: 68px; font-weight: 700; letter-spacing: 3px; line-height: 1; }
  .origin-rule { position: absolute; left: 80px; right: 80px; top: 306px; border-top: 2px solid var(--ink); }

  /* Right wrap panel */
  .nutrition { position: absolute; left: 926px; top: 84px; width: 234px; border: 3px solid var(--ink); font-size: 15.5px; }
  .nutrition-head { padding: 5px 4px 3px; border-bottom: 3px solid var(--ink); line-height: 21px; }
  .nutrition-head strong { font-weight: 700; }
  .nutrition-row { display: flex; justify-content: space-between; padding: 1px 4px; border-bottom: 2px solid var(--ink); line-height: 20px; }
  .nutrition-row:last-child { border-bottom: 0; }
  .info { position: absolute; left: 928px; width: 232px; font-size: 16px; line-height: 22px; }
  .info h2 { font-size: 16px; font-weight: 500; letter-spacing: 0.5px; }
  .expiry { top: 286px; height: 59px; border-bottom: 2px solid var(--ink); }
  .maker { top: 366px; }
  .maker h2 { margin-bottom: 4px; }
</style>
</head>
<body>
<main class="label">
  <section class="story">
    <h2 class="story-title">100% Natural</h2>
    <p>Lorem ipsum dolor sit amet, consect etuer adipi scing elit, wisi sed diam nonummy nibh euismod tincidunt ut laoreet dolore magna a aliquam erat ed volutpat. Ut wisi enim ad minim veniam, quis nostrud ad exerci tation ullamcorper suscipit lobortis aden nisl ut</p>
    <p>Aliquip exes ea commodo vel consequat. Duis autem ad vel eum iriure dolor in hendrerit molestie consequat, vel illum.</p>
  </section>

  <div class="floral-field" role="img" aria-label="Black ink engraving of wild roses, buds and serrated leaves"></div>
  <div class="front-panel"></div>

  <section class="front-card">
    <span class="corner tl"></span><span class="corner tr"></span>
    <span class="corner bl"></span><span class="corner br"></span>
    <div class="brand-name"><span class="brand-mark"></span>Sawgrass Apiary</div>
    <div class="divider"></div>
    <h1 class="product">HONEY</h1>
    <p class="variety">Wildflower Honey</p>
    <p class="claim">100% Pure &amp; Unfiltered</p>
    <p class="origin">Florida</p>
    <div class="origin-rule"></div>
  </section>

  <section class="nutrition">
    <div class="nutrition-head"><strong>NUTRITION FACTS</strong><br>Serving size&nbsp; 1 Tbsp (0.72cc)<br>Amount per serving</div>
    <div class="nutrition-row"><span>Calories 60</span></div>
    <div class="nutrition-row"><span>Total fat 0g</span><span>0%</span></div>
    <div class="nutrition-row"><span>protein 0g</span><span>0%</span></div>
    <div class="nutrition-row"><span>carbohydrates 17g</span><span>6%</span></div>
  </section>

  <section class="info expiry">
    <h2>EXPIRATION DATE</h2>
    <p>Lot.</p>
  </section>
  <section class="info maker">
    <h2>MANUFACTURED BY</h2>
    <p>www.sawgrassapiary.com</p>
    <p>hello@sawgrassapiary.com</p>
  </section>
</main>
</body>
</html>
```